LETTERHEAD & ENVELOPE: eye-catching stationary design for our custom office furniture business

Our company recently rebranded and we are in need of new stationary. Specifically, we need branded letterhead for standard paper size (8.5” x 11”), and matching envelopes, size: #9.

All designs should incorporate our brand colors, brand typeface, and logo. Please view attached brand guidelines document for brand colors, and brand description.

Letterhead: 8.5” x 11” Must include CoralvexKTN Logo, Dorrit Falke Certified Dealer Logo, mailing address, phone number, website, and email address.

Envelope: 9.5” x 4.125” Must include CoralvexKTN Logo, mailing address, and Dorrit Falke Certified Dealer Logo.

Attached files include:

```html
<!DOCTYPE html>
<html lang="en">
<head>
<meta charset="utf-8">
<title>CoralvexKTN Stationery – Letterhead &amp; Envelope</title>
<link href="https://fonts.googleapis.com/css2?family=Poppins:wght@500;600&family=Montserrat:wght@300;400;600;700&family=Fira+Sans:wght@400;600&family=Roboto+Condensed:wght@300;500&display=swap" rel="stylesheet">
<style>
  :root {
    --stage: #0b5268;
    --paper: #ffffff;
    --brand-green: #527c70;
    --brand-blue: #2f6b85;
    --slate: #3e6f87;
    --sage: #93b4a9;
    --rust: #c9432a;
    --gold: #f1c45b;
    --ink: #333333;
    --body: #666666;
    --badge-text: #5a5a5a;
    --badge-mark: #6f6f6f;
  }
  * { margin: 0; padding: 0; box-sizing: border-box; }
  html, body { width: 1200px; height: 1200px; overflow: hidden; background: var(--stage); }
  .stage { position: relative; width: 1200px; height: 1200px; }

  /* Presentation labels */
  .spec { position: absolute; color: #fff; font-family: "Poppins", sans-serif; font-weight: 600; }
  .spec-title { font-size: 34px; }
  .spec-heading { font-size: 38px; letter-spacing: 0.5px; }
  .spec-line { font-size: 22px; font-weight: 500; line-height: 34px; }

  /* Sheets */
  .sheet { position: absolute; background: var(--paper); overflow: hidden; font-family: "Montserrat", sans-serif; }
  .letterhead { left: 31px; top: 78px; width: 540px; height: 702px; }
  .envelope { left: 29px; top: 805px; width: 685px; height: 279px; }
  .abs { position: absolute; }

  .brand-mark { position: absolute; border-radius: 50%; background: var(--brand-green); }
  .brand-name { position: absolute; font-family: "Montserrat", sans-serif; font-weight: 300; color: var(--brand-green); white-space: nowrap; line-height: 1; }

  .divider { position: absolute; width: 1px; background: #999; }
  .contact { position: absolute; font-family: "Fira Sans", sans-serif; color: var(--ink); white-space: nowrap; }
  .contact b { color: var(--brand-green); font-weight: 600; }
  .contact-title { font-family: "Fira Sans", sans-serif; font-weight: 600; color: var(--brand-green); }

  .recipient { left: 31px; top: 163px; font-size: 7.5px; color: var(--ink); line-height: 1.5; }
  .recipient .name { font-size: 11.5px; font-weight: 700; color: var(--brand-blue); line-height: 1.3; }
  .recipient .role { font-weight: 700; }
  .date { right: 30px; top: 183px; font-size: 8.5px; color: var(--ink); font-weight: 600; }
  .date span { color: var(--brand-blue); font-weight: 700; }

  .letter-body { left: 31px; top: 232px; width: 479px; font-size: 8.2px; line-height: 13.3px; color: var(--body); text-align: justify; }
  .letter-body p { margin-bottom: 13.3px; }

  .signature { left: 31px; top: 500px; width: 146px; height: 24px; background: linear-gradient(90deg, #e6eeeb, #f5f8f7); }
  .signer { left: 31px; top: 536px; }
  .signer .name { font-size: 12px; font-weight: 600; color: var(--brand-blue); letter-spacing: 0.4px; }
  .signer .role { font-size: 9px; font-weight: 700; color: #222; margin-top: 3px; }

  .footer-band { position: absolute; left: 0; bottom: 0; }
  .dealer-name { font-family: "Roboto Condensed", sans-serif; font-weight: 500; fill: var(--badge-text); }
</style>
</head>
<body>
<main class="stage">

  <!-- Letterhead -->
  <section class="sheet letterhead" aria-label="Letterhead 8.5 by 11 inches">
    <div class="brand-mark" style="left:31px; top:39px; width:34px; height:34px;"></div>
    <div class="brand-name" style="left:75px; top:41px; font-size:26px;">CoralvexKTN</div>

    <div class="divider" style="left:288px; top:35px; height:42px;"></div>
    <div class="contact" style="left:306px; top:41px; font-size:6.5px; line-height:12px;">
      <div><b>P:</b> 503.555.0172</div>
      <div><b>W:</b> www.coralvexktn.com</div>
      <div><b>E:</b> hello@coralvexktn.com</div>
    </div>
    <div class="divider" style="left:399px; top:35px; height:42px;"></div>
    <div class="contact" style="left:417px; top:34px; font-size:6.5px; line-height:12px;">
      <div class="contact-title" style="font-size:13px; line-height:16px;">CoralvexKTN</div>
      <div>410 NE Larkfield, Suite 118</div>
      <div>Portland, OR 97299</div>
    </div>

    <div class="abs recipient">
      <div>To</div>
      <div class="name">Owen Hale</div>
      <div class="role">CEO, BRIGHTMILL</div>
      <div><b>W:</b> www.brightmill.co</div>
    </div>
    <div class="abs date"><span>Date:</span> 24-03-2018</div>

    <div class="abs letter-body">
      <p>Lorem ipsum dolor sit amet, consectetur adipiscing elit. Pellentesque dictum, ante non ullamcorp er convallis, nunc quam blandit metus, ac mollis eros felis a orci. Donec congue, mauris ut pulvinar lobortis, dolor massa feugiat nisi, at tincidunt metus leo vel elit. Proin facilisis semper lobortis. Vivamus augue purus, cursus quis urna non, accumsan pellentesque est. Nulla in iaculis magna, quis aliqu et ex. Cras efficitur metus eget purus euismod facilisis. Proin non metus tincidunt, auctor ipsum a, tempor mi.</p>
      <p>Nulla egestas vulputate risus, ut vestibulum diam commodo id. Mauris ornare libero eu erat portt itor ultrices. Proin sed lectus scelerisque ligula bibendum sagittis ac nec leo. Donec ac accumsan diam, et lobortis mauris.</p>
      <p>Nulla congue volutpat nisl ac lobortis. Integer dignissim interdum libero, quis feugiat velit pretium at. Phasellus sit amet libero rutrum, feugiat odio et, tempus purus. Cras ultricies, leo at fringilla solli cit udin, leo sapien placerat enim, a rutrum lorem enim ut tortor. Phasellus magna ante, cong ue maximus egestas sit amet, venenatis scelerisque felis.</p>
      <p>Nulla congue volutpat nisl ac lobortis. Integer dignissim interdum libero, quis feugiat velit pretium at. Phasellus sit amet libero rutrum, feugiat odio et, tempus purus. Cras ultricies, leo at fringilla solli cit udin, leo sapien placerat enim, a rutrum lorem enim ut tortor. Phasellus magna ante, cong ue maximus egestas sit amet, venenatis scelerisque felis.</p>
    </div>

    <div class="abs signature" role="img" aria-label="Handwritten digital signature"></div>
    <div class="abs signer">
      <div class="name">OWEN HALE</div>
      <div class="role">Vice President</div>
    </div>

    <svg class="footer-band" width="540" height="37" viewBox="0 0 540 37" aria-label="Brand stripes and certified dealer badge">
      <polygon points="358,0 540,0 540,37 0,37 0,31 340,31" fill="var(--gold)"/>
      <polygon points="0,23 109,23 107,29 0,29" fill="var(--slate)"/>
      <polygon points="113,23 224,23 222,29 111,29" fill="var(--sage)"/>
      <polygon points="228,23 339,23 337,29 226,29" fill="var(--rust)"/>
      <circle cx="382" cy="17" r="10" fill="var(--badge-mark)"/>
      <text class="dealer-name" x="402" y="21" font-size="10">Dorrit Falke Certified Dealer</text>
    </svg>
  </section>

  <!-- Envelope -->
  <section class="sheet envelope" aria-label="Envelope 9.5 by 4.125 inches">
    <div class="brand-mark" style="left:21px; top:30px; width:50px; height:50px;"></div>
    <div class="brand-name" style="left:87px; top:37px; font-size:38px;">CoralvexKTN</div>

    <div class="contact" style="left:21px; top:132px; font-size:10.5px; line-height:15px;">
      <div><b>P:</b> 503.555.0172</div>
      <div><b>W:</b> www.coralvexktn.com</div>
      <div><b>E:</b> hello@coralvexktn.com</div>
    </div>
    <div class="contact" style="left:21px; top:193px; font-size:10.5px; line-height:15px;">
      <div class="contact-title" style="font-size:16px; line-height:19px;">CoralvexKTN</div>
      <div>410 NE Larkfield, Suite 118</div>
      <div>Portland, OR 97299</div>
    </div>

    <svg class="footer-band" width="685" height="46" viewBox="0 0 685 46" aria-label="Brand stripes and certified dealer badge">
      <polygon points="495,0 685,0 685,46 0,46 0,38 473,38" fill="var(--gold)"/>
      <polygon points="0,29 159,29 156,36 0,36" fill="var(--slate)"/>
      <polygon points="162,29 308,29 305,36 159,36" fill="var(--sage)"/>
      <polygon points="311,29 459,29 456,36 308,36" fill="var(--rust)"/>
      <circle cx="498" cy="22" r="14" fill="var(--badge-mark)"/>
      <text class="dealer-name" x="521" y="27" font-size="13">Dorrit Falke Certified Dealer</text>
    </svg>
  </section>

  <!-- Specification labels -->
  <div class="spec spec-title" style="left:614px; top:68px;">Mockup - 2</div>
  <div class="spec spec-heading" style="left:618px; top:128px;">Letterhead- 8.5”X11”</div>
  <div class="spec spec-line" style="left:617px; top:191px;">Color Mode: CMYK<br>High Quality PDF, EPS, JPG, PNG &amp; TIFF</div>

  <div class="spec spec-heading" style="left:731px; top:796px;">Envelope- 9.5”X4.125”</div>
  <div class="spec spec-line" style="left:735px; top:853px;">Color Mode: CMYK<br>High Quality PDF, EPS,<br>JPG, PNG &amp; TIFF</div>

</main>
</body>
</html>
```